Cage Free Dog Resort under new ownership needs New Logo & Website Redesign

We need a logo design and updated website for our new business. We offer cage free boarding services for dogs where they are free to run & play outside during the day. The current website has lots of brown & orange & we would like the new website to be more visually attractive utilizing more pictures of dogs playing and having fun.

Target Market(s)

Dog lovers with disposable income to afford special care for their pets - looking for a place for their dogs to be pampered while they are away from home. Primarily dogs, but we will also board cats and other pets too.

Industry/Entity Type

Pet Care

Logo Text

Willow Creek Pet Lodge

Coding

Coded - Design and coding required

Number of Pages Required

5+ page

Font styles to use
Sans Serif

Colors
0692cd
fbee3d
f04a50

Requirements
Must have
• Current website is www.willowcreekpetlodge.example
• I would like for someone to click on our website & have the "oh that is so cute/awesome/what a great looking place" reaction!
• Link to pages with forms
• Stock photos of different breeds of dogs having fun playing out doors
• Gallery Photo page (where I can go in and update with new pictures)
Nice to have
• Tag line something like - "Your best friend's home away from home!"
• Some cartoon type dogs/cats
Should not have
• Wasn't sure about font below - so whichever font is easiest to read and still looks professional

```html
<!DOCTYPE html>
<html lang="en">
<head>
<meta charset="utf-8">
<title>Willow Creek Pet Lodge &amp; Doggie Daycare</title>
<link rel="stylesheet" href="https://fonts.googleapis.com/css2?family=Oswald:wght@500;600&family=Open+Sans:wght@400;600;700&display=swap">
<style>
  :root {
    --brand-red: #dc3c4a;
    --brand-red-deep: #c92f3d;
    --brand-red-soft: #e6515d;
    --brand-blue: #0692cd;
    --brand-yellow: #fbee3d;
    --ink: #222222;
    --body-text: #3a3a3a;
    --nav-text: #444444;
    --white: #ffffff;
    --grass: #6f9a34;
    --grass-light: #a6c85a;
    --sky-light: #bfe3f3;
  }
  * { box-sizing: border-box; margin: 0; padding: 0; }
  html, body { width: 1200px; height: 3429px; overflow: hidden; }
  body {
    position: relative;
    background: var(--white);
    font-family: "Open Sans", Arial, sans-serif;
    color: var(--body-text);
  }
  .abs { position: absolute; }

  /* Header */
  .site-header { left: 0; top: 0; width: 1200px; height: 105px; background: var(--white); }
  .brand { left: 126px; top: 24px; display: flex; align-items: center; gap: 14px; }
  .brand-mark { width: 48px; height: 48px; border-radius: 50%; background: var(--brand-red); flex: none; }
  .brand-name {
    font-family: "Open Sans", Arial, sans-serif; font-weight: 700; font-size: 20px;
    line-height: 27px; color: var(--brand-red); text-transform: uppercase; letter-spacing: 0.2px;
  }
  .btn {
    display: flex; align-items: center; justify-content: center;
    background: var(--brand-red); color: var(--white);
    font-family: "Open Sans", Arial, sans-serif; font-weight: 700; font-size: 15px;
    text-transform: uppercase; border-radius: 6px; letter-spacing: 0.3px;
  }
  .btn-quote { left: 891px; top: 18px; width: 183px; height: 44px; font-size: 14px; }
  .main-nav { right: 126px; top: 76px; display: flex; gap: 30px; font-size: 13px; font-weight: 600; color: var(--nav-text); }

  /* Hero */
  .hero {
    left: 0; top: 105px; width: 1200px; height: 524px;
    clip-path: polygon(0 0, 100% 0, 100% 444px, 50% 524px, 0 444px);
  }
  .hero-photo {
    width: 100%; height: 100%;
    background:
      radial-gradient(ellipse 260px 200px at 470px 330px, rgba(201,60,74,0.55), rgba(201,60,74,0) 70%),
      radial-gradient(ellipse 300px 160px at 820px 300px, rgba(251,238,61,0.35), rgba(251,238,61,0) 70%),
      radial-gradient(ellipse 420px 180px at 160px 260px, rgba(120,84,50,0.55), rgba(120,84,50,0) 70%),
      linear-gradient(180deg, var(--sky-light) 0%, #7fb6cf 16%, #7c8c5c 34%, var(--grass) 62%, #4f7326 100%);
  }
  .hero-title {
    left: 596px; top: 254px; font-family: "Oswald", Arial, sans-serif; font-weight: 600;
    font-size: 45px; line-height: 61px; color: var(--white); text-transform: uppercase;
    text-shadow: 0 2px 6px rgba(0,0,0,0.35);
  }
  .btn-contact { left: 599px; top: 402px; width: 164px; height: 53px; font-size: 18px; border: 2px solid var(--white); border-radius: 4px; }

  /* Section headings */
  .section-title {
    font-family: "Oswald", Arial, sans-serif; font-weight: 600; font-size: 38px;
    line-height: 46px; text-transform: uppercase; color: var(--ink);
  }

  /* About */
  .about-title { left: 126px; top: 727px; }
  .about-text { left: 126px; top: 793px; width: 411px; font-size: 12px; line-height: 23px; text-align: justify; }
  .btn-read-about { left: 126px; top: 1026px; width: 135px; height: 46px; font-size: 14px; }
  .about-photo {
    left: 558px; top: 731px; width: 516px; height: 348px; border-radius: 6px;
    background:
      radial-gradient(ellipse 90px 80px at 235px 200px, rgba(35,35,45,0.75), rgba(35,35,45,0) 75%),
      radial-gradient(ellipse 300px 120px at 420px 20px, rgba(251,238,61,0.65), rgba(251,238,61,0) 75%),
      linear-gradient(180deg, #f6f1c2 0%, #cfe07a 26%, var(--grass-light) 48%, var(--grass) 100%);
  }

  /* Rates */
  .rates {
    left: 0; top: 1154px; width: 1200px; height: 526px;
    background:
      radial-gradient(ellipse 260px 170px at 330px 300px, rgba(255,255,255,0.10), rgba(255,255,255,0) 70%),
      radial-gradient(ellipse 300px 200px at 900px 360px, rgba(150,20,35,0.18), rgba(150,20,35,0) 70%),
      linear-gradient(135deg, var(--brand-red-soft) 0%, var(--brand-red) 50%, var(--brand-red-deep) 100%);
    clip-path: polygon(0 0, 38% 74px, 72% 74px, 100% 0, 100% 100%, 0 100%);
  }
  .rates-title { left: 0; width: 1200px; top: 1344px; text-align: center; color: var(--white); }
  .rates-text { left: 222px; top: 1420px; width: 756px; text-align: center; color: var(--white); font-size: 12px; line-height: 25px; }
  .btn-outline { background: transparent; border: 1.5px solid var(--white); border-radius: 4px; font-size: 14px; }
  .btn-read-rates { left: 537px; top: 1527px; width: 126px; height: 46px; }

  /* Gallery */
  .gallery-title { left: 0; width: 1200px; top: 1805px; text-align: center; }
  .gallery-text { left: 250px; top: 1873px; width: 700px; text-align: center; font-size: 12px; line-height: 25px; }
  .gallery-mascot {
    left: 976px; top: 1712px; width: 190px; height: 264px; border-radius: 46% 46% 40% 40%;
    background: radial-gradient(circle at 50% 38%, var(--brand-yellow) 0%, #f3b35a 35%, #e08a2c 70%, #f6e3c4 100%);
  }
  .gallery-item { border-radius: 50%; }
  .gallery-item.featured { left: 108px; top: 2027px; width: 334px; height: 334px; border: 3px solid var(--white); box-shadow: 0 4px 18px rgba(0,0,0,0.35); }
  .gi-1 {
    background:
      radial-gradient(circle at 40% 50%, rgba(95,80,70,0.9), rgba(95,80,70,0) 35%),
      radial-gradient(circle at 72% 58%, rgba(230,120,40,0.85), rgba(230,120,40,0) 18%),
      linear-gradient(160deg, #6f9a3a, #8a6a4a 55%, #4f6f2a);
  }
  .gi-2 {
    left: 489px; top: 2068px; width: 252px; height: 252px;
    background:
      radial-gradient(circle at 50% 45%, rgba(240,215,160,0.95), rgba(240,215,160,0) 24%),
      linear-gradient(180deg, #eaf5fa 0%, #8ccbe8 40%, var(--brand-blue) 70%, #d8c9a2 100%);
  }
  .gi-3 {
    left: 823px; top: 2068px; width: 252px; height: 252px;
    background:
      radial-gradient(circle at 35% 60%, rgba(110,60,40,0.8), rgba(110,60,40,0) 18%),
      radial-gradient(circle at 70% 25%, rgba(251,238,61,0.9), rgba(251,238,61,0) 12%),
      linear-gradient(180deg, #c3d59a, #8fb356 50%, #5b7c2c);
  }
  .gi-4 {
    left: 126px; top: 2432px; width: 252px; height: 252px;
    background:
      radial-gradient(circle at 55% 50%, rgba(215,130,60,0.9), rgba(215,130,60,0) 22%),
      radial-gradient(circle at 25% 80%, rgba(251,238,61,0.6), rgba(251,238,61,0) 20%),
      linear-gradient(180deg, #eef0dc, #b3cf72 45%, #6e9434);
  }
  .gi-5 {
    left: 475px; top: 2432px; width: 252px; height: 252px;
    background:
      radial-gradient(circle at 45% 55%, rgba(200,170,130,0.9), rgba(200,170,130,0) 26%),
      linear-gradient(180deg, #d8d2c6, #bdb6a8 55%, #9fb4c0);
  }
  .gi-6 {
    left: 823px; top: 2432px; width: 252px; height: 252px;
    background:
      radial-gradient(circle at 55% 60%, rgba(40,35,35,0.9), rgba(40,35,35,0) 22%),
      linear-gradient(180deg, #e3f2fa 0%, #8fcbe6 28%, var(--brand-blue) 48%, #d5c8ab 70%, #bcae90 100%);
  }
  .btn-view-more { left: 533px; top: 2771px; width: 134px; height: 48px; font-size: 14px; }

  /* Newsletter */
  .newsletter {
    left: 0; top: 2800px; width: 1200px; height: 629px;
    background:
      radial-gradient(ellipse 320px 200px at 700px 470px, rgba(150,20,35,0.16), rgba(150,20,35,0) 70%),
      linear-gradient(160deg, var(--brand-red-soft) 0%, var(--brand-red) 55%, var(--brand-red-deep) 100%);
    clip-path: polygon(0 0, 50% 153px, 100% 0, 100% 100%, 0 100%);
  }
  .newsletter-title { left: 0; width: 1200px; top: 3064px; text-align: center; color: var(--white); }
  .newsletter-text { left: 222px; top: 3136px; width: 756px; text-align: center; color: var(--white); font-size: 12px; line-height: 25px; }
  .subscribe-form { left: 366px; top: 3237px; width: 466px; height: 44px; display: flex; }
  .email-field {
    flex: 1; background: var(--white); border-radius: 5px 0 0 5px; font-size: 12px;
    color: #555; padding-left: 26px; display: flex; align-items: center;
  }
  .btn-subscribe { width: 123px; border-radius: 0 5px 5px 0; border: 1.5px solid var(--white); font-size: 14px; background: var(--brand-red); }

  /* Footer */
  .footer-rule { left: 126px; top: 3354px; width: 948px; height: 1px; background: rgba(255,255,255,0.6); }
  .copyright { left: 126px; top: 3377px; font-size: 12px; color: var(--white); }
  .social { left: 963px; top: 3370px; display: flex; gap: 10px; }
  .social span { width: 30px; height: 30px; border-radius: 50%; border: 1.5px solid var(--white); }
</style>
</head>
<body>

<header class="site-header abs">
  <div class="brand abs">
    <span class="brand-mark"></span>
    <span class="brand-name">Willow Creek Pet Lodge<br>&amp; Doggie Daycare</span>
  </div>
  <a class="btn btn-quote abs">Request a Quote</a>
  <nav class="main-nav abs">
    <span>Home</span><span>About Us</span><span>Rates &amp; Hours</span><span>Accommodation</span><span>Contact Us</span>
  </nav>
</header>

<section class="hero abs">
  <div class="hero-photo" role="img" aria-label="Photo of a caretaker with a group of dogs playing around a slide in a fenced grassy play yard"></div>
</section>
<h1 class="hero-title abs">Your best friend's home<br>away from home!</h1>
<a class="btn btn-contact abs">Contact Us</a>

<h2 class="section-title about-title abs">About Us</h2>
<p class="about-text abs">Willow Creek Pet Lodge is a cage free resort where dogs spend their days running, playing and resting in wide open yards under the watchful eyes of our caring team. Every guest enjoys meals on their own schedule, plenty of fresh water, shady spots to nap and cosy indoor suites for quiet evenings. We keep play groups small and matched by size and temperament, so shy pups and bold ones both feel safe. Cats and other small pets are welcome too, with peaceful rooms of their own far from the busy yards. Your best friend comes home tired and happy.</p>
<a class="btn btn-read-about abs">Read More</a>
<div class="about-photo abs" role="img" aria-label="Photo of a small dog running across a sunny lawn after a flying disc"></div>

<section class="rates abs" role="img" aria-label="Red tinted photo of dogs in the play yard"></section>
<h2 class="section-title rates-title abs">Rates and Hours</h2>
<p class="rates-text abs">Day play, overnight boarding and longer holiday stays are all priced simply, with generous discounts for families with multiple pets and for weekly bookings. We are open seven days a week for drop off and pick up, with extended hours during school breaks and public holidays, so your best friend is never left waiting for you. Baths, nail trims and extra play sessions can be added to any stay.</p>
<a class="btn btn-outline btn-read-rates abs">Read More</a>

<h2 class="section-title gallery-title abs">Our Gallery</h2>
<p class="gallery-text abs">Take a peek at our guests enjoying the sunshine, chasing balls, splashing in the pool and making new friends every single day at the lodge. We add fresh photos every week so you can see how much fun your pup is having while you are away, and share favourite moments with family too.</p>
<div class="gallery-mascot abs" role="img" aria-label="Cartoon illustration of a sitting puppy with a red collar"></div>

<div class="gallery-item featured gi-1 abs" role="img" aria-label="Photo of two dogs playing tug with a rope toy"></div>
<div class="gallery-item gi-2 abs" role="img" aria-label="Photo of a retriever running through shallow water with a ball"></div>
<div class="gallery-item gi-3 abs" role="img" aria-label="Photo of dogs playing with toys on a grassy field"></div>
<div class="gallery-item gi-4 abs" role="img" aria-label="Photo of a collie running through a flower meadow"></div>
<div class="gallery-item gi-5 abs" role="img" aria-label="Photo of puppies resting in the sand"></div>
<div class="gallery-item gi-6 abs" role="img" aria-label="Photo of a dark dog standing on a beach by the sea"></div>
<a class="btn btn-view-more abs">View More</a>

<section class="newsletter abs" role="img" aria-label="Red tinted photo of dogs at play"></section>
<h2 class="section-title newsletter-title abs">Subscribe Newsletter</h2>
<p class="newsletter-text abs">Join our mailing list for seasonal offers, holiday booking reminders, helpful pet care tips and the newest photos of our happy guests delivered straight to your inbox each month.</p>
<div class="subscribe-form abs">
  <span class="email-field">Enter Email Address</span>
  <a class="btn btn-subscribe">Subscribe</a>
</div>

<footer>
  <div class="footer-rule abs"></div>
  <p class="copyright abs">Copyrights © 2018. All Rights Reserved</p>
  <div class="social abs" aria-label="Social links"><span></span><span></span><span></span></div>
</footer>

</body>
</html>
```